Modern, pro female massage business needs business card design

We are a boutique, pro women's sports and remedial massage studio based in Singapore - we have a logo already (see attached image) and need to design a business card that reflects an elegant, modern and feminine feel using this logo.

We are focussed on a very local market and need to give a professional yet warm feeling.

Details for the card include (layout of your choice):

Talvina Brisk
Call, SMS or ChatBeam: 8317 6092
Email: tealmarrow@quenfold.com
Address: The Harbourview at Dunmore
82 Dunmore Road, East Coast, Singapore

To incorporate the OVAR logo (www.ovarglobe.co.uk) would be appreciated - see attached file.

Industry/Entity Type

Massage

Requirements
Nice to have
• We like the idea of using an embossed style card. Solid colour on the reverse - embossed on the front; four colour printing is okay.
Should not have
• It should not be uber 'girly girl' if that makes any sense. The logo is already colourful

```html
<!DOCTYPE html>
<html lang="en">
<head>
<meta charset="utf-8">
<title>tealmarrow – Business Card</title>
<link rel="stylesheet" href="https://fonts.googleapis.com/css2?family=Lato:wght@400;700;900&family=Arvo:wght@400&display=swap">
<style>
  :root {
    --canvas: #d9d9dc;
    --card-dark: #1f2a33;
    --card-dark-edge: #2a3742;
    --brand-pink: #e2197f;
    --panel-pink: #e0388f;
    --lime: #a6cc2e;
    --tagline-grey: #5e6870;
    --text-light: #ffffff;
    --badge-blue: #2f6fb5;
    --badge-frame: #e8eef5;
    --logo-font: "Lato", sans-serif;
    --detail-font: "Arvo", serif;
  }
  * { box-sizing: border-box; margin: 0; padding: 0; }
  html, body {
    width: 1200px;
    height: 900px;
    overflow: hidden;
    background: var(--canvas);
  }
  .canvas {
    position: relative;
    width: 1200px;
    height: 900px;
  }
  .card {
    position: absolute;
    left: 250px;
    width: 700px;
    height: 400px;
    border-radius: 6px;
    overflow: hidden;
    background: var(--card-dark);
    box-shadow: 0 6px 18px rgba(0, 0, 0, 0.22);
  }
  .card--back { top: 40px; }
  .card--front { top: 460px; }
  .card__shapes {
    position: absolute;
    inset: 0;
    width: 100%;
    height: 100%;
  }

  /* Brand name + tagline */
  .brand {
    position: absolute;
    text-align: left;
  }
  .brand__name {
    font-family: var(--logo-font);
    font-weight: 900;
    color: var(--brand-pink);
    letter-spacing: -1px;
    line-height: 1;
  }
  .brand__tagline {
    font-family: var(--logo-font);
    font-weight: 400;
    color: var(--tagline-grey);
    line-height: 1;
  }
  .card--back .brand {
    left: 140px;
    top: 130px;
  }
  .card--back .brand__name { font-size: 84px; }
  .card--back .brand__tagline { font-size: 27px; margin-top: 4px; padding-left: 6px; }

  .card--front .brand {
    left: 230px;
    top: 34px;
  }
  .card--front .brand__name { font-size: 56px; }
  .card--front .brand__tagline { font-size: 18px; margin-top: 2px; padding-left: 4px; }

  /* Partner badge */
  .partner-badge {
    position: absolute;
    right: 42px;
    top: 118px;
    width: 42px;
    height: 42px;
    background: var(--badge-blue);
    border: 3px solid var(--badge-frame);
  }

  /* Contact details */
  .contact {
    position: absolute;
    left: 40px;
    top: 246px;
    font-family: var(--detail-font);
    color: var(--text-light);
  }
  .contact__name {
    font-size: 25px;
    margin-bottom: 6px;
  }
  .contact__line {
    font-size: 17px;
    line-height: 1.45;
  }
  .label {
    color: var(--lime);
    font-size: 13px;
  }

  .address {
    position: absolute;
    right: 40px;
    top: 196px;
    text-align: right;
    font-family: var(--detail-font);
    color: var(--text-light);
    font-size: 16px;
    line-height: 1.55;
  }
  .address__street { font-size: 17px; }
</style>
</head>
<body>
<main class="canvas">

  <!-- Reverse side: solid colour with brand name -->
  <section class="card card--back" aria-label="Business card, reverse">
    <div class="brand">
      <div class="brand__name">tealmarrow</div>
      <div class="brand__tagline">Remedial and sports massage</div>
    </div>
  </section>

  <!-- Front side: contact details -->
  <section class="card card--front" aria-label="Business card, front">
    <svg class="card__shapes" viewBox="0 0 700 400" preserveAspectRatio="none" aria-hidden="true">
      <path d="M0,262 C170,200 390,190 560,120 C620,95 670,68 700,50 L700,400 L0,400 Z" fill="var(--panel-pink)"/>
      <path d="M150,222 C330,192 470,176 580,118 C630,92 670,68 700,46"
            fill="none" stroke="var(--lime)" stroke-width="4" stroke-linecap="round"/>
      <path d="M0,392 C60,330 170,290 330,262 C250,282 110,330 0,400 Z" fill="var(--lime)"/>
    </svg>

    <div class="brand">
      <div class="brand__name">tealmarrow</div>
      <div class="brand__tagline">Remedial and sports massage</div>
    </div>

    <div class="partner-badge" role="img" aria-label="Accreditation badge"></div>

    <div class="contact">
      <div class="contact__name">Talvina Brisk</div>
      <div class="contact__line"><span class="label">Call, SMS or ChatBeam:</span> 8317 6092</div>
      <div class="contact__line"><span class="label">Email:</span> tealmarrow@quenfold.com</div>
    </div>

    <div class="address">
      <div><span class="label">Address:</span> The Harbourview at Dunmore</div>
      <div class="address__street">82 Dunmore Road, East Coast, Singapore</div>
    </div>
  </section>

</main>
</body>
</html>
```